Ward Compass Business Card Design*

We need a business card design for our company Ward Compass. Our company is specialized in providing online consulting services regarding medical institutions, hospitals and doctors. We work with patients worldwide looking to choose between healthcare providers. We have a website you may use as a reference, where we list doctors and clinics worldwide. So we target Medical providers as well as patients worldwide.
Target Market(s)
Medical Providers and patients around the world
Industry/Entity Type
Medical
Contact Information for Business Card
Salma Derkaoui
CEO
+90 612 348 2071
info@wardcompass-example.com
www.wardcompass-example.com
14 Annakhil 3 H.R.B. Rabat, Morocco
Requirements
Must have
- Company logo/name on one full side, personal info and smaller logo and company name on the other side.
Nice to have
- Smart and elegant design

```html
<!DOCTYPE html>
<html lang="en">
<head>
<meta charset="utf-8">
<title>Ward Compass Business Card</title>
<link href="https://fonts.googleapis.com/css2?family=Montserrat:wght@300;400;500;700&family=Lato:wght@400;700&display=swap" rel="stylesheet">
<style>
  :root {
    --stage: #262626;
    --navy: #0d3166;
    --ink-navy: #163a78;
    --violet: #2e2a6b;
    --grey: #8a8a8a;
    --light-grey: #a9a9a9;
    --paper: #ffffff;
    --text: #2b2b2b;
  }
  * { margin: 0; padding: 0; box-sizing: border-box; }
  html, body { width: 1200px; height: 900px; overflow: hidden; background: var(--stage); }
  .canvas { position: relative; width: 1200px; height: 900px; }
  .card {
    position: absolute; left: 250px; width: 700px; height: 400px;
    overflow: hidden; box-shadow: 0 12px 30px rgba(0,0,0,.45);
  }
  .card--front { top: 40px; background: var(--navy); }
  .card--back { top: 470px; background: var(--paper); }

  .brand { display: flex; align-items: center; gap: 18px; font-family: "Montserrat", sans-serif; }
  .brand__dot { border-radius: 50%; flex: none; }
  .brand__name { font-weight: 500; text-transform: uppercase; white-space: nowrap; }

  .card--front .brand { position: absolute; left: 150px; top: 150px; }
  .card--front .brand__dot { width: 64px; height: 64px; background: var(--paper); }
  .card--front .brand__name { color: var(--paper); font-size: 44px; letter-spacing: 3px; }
  .front__web {
    position: absolute; left: 0; right: 0; top: 320px; text-align: center;
    font-family: "Montserrat", sans-serif; font-weight: 500; font-size: 15px;
    letter-spacing: 4px; color: var(--paper);
  }

  .card--back .brand { position: absolute; right: 60px; top: 60px; gap: 12px; }
  .card--back .brand__dot { width: 34px; height: 34px; background: var(--ink-navy); }
  .card--back .brand__name { color: var(--ink-navy); font-size: 22px; letter-spacing: 1.5px; }

  .swoosh { position: absolute; inset: 0; width: 700px; height: 400px; }
  .swoosh__band { fill: var(--violet); }
  .swoosh__line { fill: var(--grey); }

  .person { position: absolute; left: 70px; top: 205px; font-family: "Montserrat", sans-serif; }
  .person__name { font-size: 22px; letter-spacing: .5px; }
  .person__first { font-weight: 700; color: var(--ink-navy); }
  .person__last { font-weight: 300; color: var(--light-grey); }
  .person__role { font-family: "Lato", sans-serif; font-size: 13px; color: var(--text); margin-top: 2px; }
  .contact { list-style: none; margin-top: 26px; font-family: "Lato", sans-serif; font-size: 17px; color: var(--text); }
  .contact li { display: flex; align-items: center; gap: 12px; margin-bottom: 8px; }
  .contact svg { width: 18px; height: 18px; fill: var(--ink-navy); flex: none; }
</style>
</head>
<body>
<main class="canvas">
  <section class="card card--front" aria-label="Card front">
    <div class="brand">
      <span class="brand__dot"></span>
      <span class="brand__name">Ward Compass</span>
    </div>
    <p class="front__web">www.wardcompass-example.com</p>
  </section>

  <section class="card card--back" aria-label="Card back">
    <svg class="swoosh" viewBox="0 0 700 400" aria-hidden="true">
      <path class="swoosh__band" d="M0,400 L0,388 Q420,372 700,175 L700,400 Z"/>
      <path class="swoosh__line" d="M280,376 Q500,352 700,140 L700,162 Q490,355 280,376 Z"/>
    </svg>
    <div class="brand">
      <span class="brand__dot"></span>
      <span class="brand__name">Ward Compass</span>
    </div>
    <div class="person">
      <p class="person__name"><span class="person__first">SALMA</span> <span class="person__last">DERKAOUI</span></p>
      <p class="person__role">CEO</p>
      <ul class="contact">
        <li>
          <svg viewBox="0 0 24 24"><path d="M6.6 10.8a15.1 15.1 0 0 0 6.6 6.6l2.2-2.2c.3-.3.7-.4 1-.2 1.1.4 2.3.6 3.6.6.6 0 1 .4 1 1V20c0 .6-.4 1-1 1A17 17 0 0 1 3 4c0-.6.4-1 1-1h3.5c.6 0 1 .4 1 1 0 1.3.2 2.5.6 3.6.1.3 0 .7-.2 1z"/></svg>
          +90 612 348 2071
        </li>
        <li>
          <svg viewBox="0 0 24 24"><path d="M3 5h18v14H3z M4.5 6.5 12 12l7.5-5.5" stroke="#fff" stroke-width="1.4"/></svg>
          info@wardcompass-example.com
        </li>
      </ul>
    </div>
  </section>
</main>
</body>
</html>
```